Business Card Design

We need a new business card design for our company, Lumen Forge.

Our website: www.brightrow7.ca

We are open to all ideas, from professional to very creative.
Updates

Design update requests:

1. We would like to see some examples with "BrightRow7" instead of "Lumen Forge" as the company name.
2. Would like to see "Software | Web | Branding" included on the card somewhere as well.

Thanks.

We are really trying to express the nature of our business through our business card.  "Lumen" can be misconstrued for the health industry, so use of "BrightRow7" and the "Software | Web | Branding" slogan are key to understanding our business.

We have uploaded a new PSD which includes a monitor, tablet, and phone screen.  This represents the flexibility of web applications and is another tool we would like to see used on business cards.

We will be eliminating designs today and will await updated designs with these new specs.

Thank-you.

Industry/Entity Type

Business

Requirements
Must have
• Content:
First M. Last
Managing Partner
e. email@brightrow7.ca
p. 555.555.5555

```html
<!DOCTYPE html>
<html lang="en">
<head>
<meta charset="utf-8">
<title>BrightRow7 Business Card</title>
<link rel="stylesheet" href="https://fonts.googleapis.com/css2?family=Open+Sans:wght@400;600;700;800&display=swap">
<style>
  :root {
    --page-bg: #e6e6ea;
    --card-bg: #ffffff;
    --ink-dark: #4a4a4c;
    --ink-teal: #1d6d8a;
    --accent-blue: #1ba7e3;
    --band-grey: #7c7c7e;
    --mark-blue: #3aa2d6;
  }
  * { box-sizing: border-box; margin: 0; padding: 0; }
  html, body {
    width: 1200px; height: 987px; overflow: hidden;
    background: var(--page-bg);
    font-family: "Open Sans", Arial, sans-serif;
  }
  .canvas { position: relative; width: 1200px; height: 987px; }
  .card {
    position: absolute;
    width: 560px; height: 320px;
    background: var(--card-bg);
    border-radius: 30px;
    overflow: hidden;
    box-shadow: 0 6px 18px rgba(0,0,0,0.12);
  }
  .card--back { left: 590px; top: 110px; }
  .card--front { left: 50px; top: 540px; }

  .brand { display: flex; flex-direction: column; align-items: flex-start; }
  .brand-row { display: flex; align-items: center; gap: 14px; }
  .brand-square { width: 34px; height: 34px; background: var(--mark-blue); flex: none; }
  .brand-name {
    font-weight: 800; font-size: 44px; line-height: 1; color: var(--ink-dark);
    letter-spacing: 1px; text-transform: uppercase;
  }
  .brand-slogan {
    margin-top: 8px; padding-left: 48px;
    font-weight: 600; font-size: 15px; letter-spacing: 1px; color: var(--accent-blue);
    white-space: nowrap;
  }

  /* back */
  .card--back .brand { position: absolute; left: 0; right: 0; top: 92px; align-items: center; }
  .card--back .brand-slogan { padding-left: 48px; }
  .back-web {
    position: absolute; left: 0; right: 0; top: 222px; text-align: center;
    font-weight: 700; font-size: 20px; letter-spacing: 6px; color: var(--ink-dark);
  }

  /* front */
  .name-bar { position: absolute; left: 24px; top: 22px; width: 9px; height: 44px; background: var(--band-grey); }
  .person-name { position: absolute; left: 46px; top: 18px; font-weight: 700; font-size: 22px; color: var(--ink-teal); }
  .person-title { position: absolute; left: 46px; top: 48px; font-size: 14px; color: var(--accent-blue); }
  .contact { position: absolute; left: 30px; top: 96px; font-size: 14px; color: var(--ink-dark); line-height: 1.35; }
  .contact-row { display: flex; gap: 8px; align-items: flex-start; margin-bottom: 14px; }
  .contact-row svg { flex: none; margin-top: 2px; }
  .card--front .brand { position: absolute; right: 34px; top: 140px; }
  .card--front .brand-square { width: 26px; height: 26px; }
  .card--front .brand-row { gap: 11px; }
  .card--front .brand-name { font-size: 32px; }
  .card--front .brand-slogan { font-size: 12px; margin-top: 7px; padding-left: 37px; }
  .bands { position: absolute; left: 0; bottom: 0; }
  .band-web {
    position: absolute; left: 28px; top: 256px;
    font-size: 16px; letter-spacing: 3px; color: #ffffff;
  }
</style>
</head>
<body>
<main class="canvas">
  <section class="card card--back" aria-label="Card back">
    <div class="brand">
      <div class="brand-row"><span class="brand-square"></span><span class="brand-name">BrightRow7</span></div>
      <p class="brand-slogan">Software | Web | Branding</p>
    </div>
    <p class="back-web">www.brightrow7.ca</p>
  </section>

  <section class="card card--front" aria-label="Card front">
    <svg class="bands" width="560" height="320" viewBox="0 0 560 320">
      <path d="M0 246 H300 Q318 246 330 258 L352 282 H0 Z" fill="var(--accent-blue)"/>
      <path d="M0 282 H352 L330 258 Q318 246 300 246 H560 V320 H0 Z" fill="var(--band-grey)"/>
    </svg>
    <span class="name-bar"></span>
    <h1 class="person-name">First M. Last</h1>
    <p class="person-title">Managing Partner</p>
    <div class="contact">
      <div class="contact-row">
        <svg width="14" height="14" viewBox="0 0 14 14"><circle cx="7" cy="7" r="7" fill="var(--ink-dark)"/><circle cx="7" cy="6" r="2.4" fill="#fff"/></svg>
        <span>00, Complex name<br>City, State 0000</span>
      </div>
      <div class="contact-row">
        <svg width="14" height="14" viewBox="0 0 14 14"><circle cx="7" cy="7" r="6" fill="none" stroke="var(--ink-dark)" stroke-width="1.5"/><path d="M5 4 L6.5 5.5 L5.8 6.6 Q6.6 8 7.6 8.4 L8.6 7.6 L10 9 L9 10.2 Q6 10 4 6 Z" fill="var(--ink-dark)"/></svg>
        <span>555.555.5555</span>
      </div>
      <div class="contact-row">
        <svg width="14" height="14" viewBox="0 0 14 14"><rect x="1" y="3" width="12" height="9" rx="1" fill="var(--ink-dark)"/><path d="M1.5 4 L7 8 L12.5 4" fill="none" stroke="#fff" stroke-width="1.2"/></svg>
        <span>email@brightrow7.ca</span>
      </div>
    </div>
    <div class="brand">
      <div class="brand-row"><span class="brand-square"></span><span class="brand-name">BrightRow7</span></div>
      <p class="brand-slogan">Software | Web | Branding</p>
    </div>
    <p class="band-web">www.brightrow7.ca</p>
  </section>
</main>
</body>
</html>
```